Cover for Where the Quiet River Bends Beyond Our Morning

Cover for a book that describes everything that happens to a person, from pre-birth life plans through growing in compassion and wisdom to death and living in the afterlife. The information is revealed in messages from people living in the life after this life. The title is Lanterns Along the Hidden Stair of Every Soul: Gathered from Voices Dwelling in the Further Meadow. Author is T. Morven Ashdale. Book size is 6 by 9.

Target Market(s)

General

Font styles to use
Serif

```html
<!DOCTYPE html>
<html lang="en">
<head>
<meta charset="utf-8">
<title>Lanterns Along the Hidden Stair of Every Soul — Book Cover</title>
<link rel="stylesheet" href="https://fonts.googleapis.com/css2?family=Poppins:wght@400;600&family=Lora:wght@700&display=swap">
<style>
  :root {
    --ink-deep: #1c181b;
    --umber: #3d342c;
    --smoke: #4a4447;
    --mist: #8a8290;
    --violet: #3e2f5c;
    --plum: #5a3f66;
    --ember: #6b4a3a;
    --band: rgba(46, 42, 44, 0.78);
    --glow-text: #f3eea4;
    --glow-halo: rgba(240, 230, 120, 0.55);
    --author: #ddd6c6;
  }
  html, body {
    margin: 0;
    padding: 0;
    width: 800px;
    height: 1200px;
    overflow: hidden;
    background: var(--ink-deep);
  }
  .cover {
    position: relative;
    width: 800px;
    height: 1200px;
    overflow: hidden;
  }
  .cover-art {
    position: absolute;
    inset: 0;
    background:
      radial-gradient(ellipse 22% 18% at 40% 34%, rgba(170, 160, 185, 0.55), transparent 72%),
      radial-gradient(ellipse 28% 26% at 58% 60%, rgba(110, 80, 160, 0.65), transparent 72%),
      radial-gradient(ellipse 20% 30% at 72% 78%, rgba(150, 140, 160, 0.45), transparent 72%),
      radial-gradient(ellipse 26% 36% at 14% 52%, rgba(120, 90, 60, 0.6), transparent 72%),
      radial-gradient(ellipse 22% 20% at 86% 26%, rgba(120, 105, 100, 0.55), transparent 72%),
      radial-gradient(ellipse 18% 16% at 78% 45%, rgba(140, 80, 90, 0.45), transparent 72%),
      radial-gradient(ellipse 30% 22% at 20% 88%, rgba(90, 75, 60, 0.6), transparent 72%),
      linear-gradient(160deg, var(--umber) 0%, var(--smoke) 30%, var(--plum) 55%, var(--violet) 72%, var(--ink-deep) 100%);
  }
  .title-band {
    position: absolute;
    left: 0;
    top: 0;
    width: 800px;
    height: 134px;
    background: var(--band);
  }
  .glow {
    position: absolute;
    left: 0;
    width: 800px;
    margin: 0;
    text-align: center;
    color: var(--glow-text);
    text-shadow: 0 0 6px var(--glow-halo), 0 0 14px var(--glow-halo);
    line-height: 1;
  }
  .kicker {
    top: 24px;
    font-family: "Poppins", sans-serif;
    font-weight: 400;
    font-size: 21px;
    letter-spacing: 1.5px;
  }
  .headline {
    top: 74px;
    font-family: "Poppins", sans-serif;
    font-weight: 600;
    font-size: 31px;
    letter-spacing: 4px;
    text-transform: uppercase;
  }
  .subline {
    font-family: "Lora", serif;
    font-weight: 700;
    font-size: 22px;
  }
  .subline-1 { top: 468px; }
  .subline-2 { top: 520px; }
  .main-title {
    top: 580px;
    font-family: "Lora", serif;
    font-weight: 700;
    font-size: 47px;
    letter-spacing: 3px;
    text-transform: uppercase;
  }
  .author {
    position: absolute;
    left: 0;
    top: 1146px;
    width: 800px;
    margin: 0;
    text-align: center;
    font-family: "Lora", serif;
    font-weight: 700;
    font-size: 22px;
    line-height: 1;
    letter-spacing: 1px;
    color: var(--author);
  }
</style>
</head>
<body>
  <main class="cover">
    <div class="cover-art" role="img" aria-label="Full-bleed dreamlike photo collage: a resting face fading into starry violet mist, with stained-glass rose window fragments and faint constellation lines"></div>
    <div class="title-band"></div>
    <p class="glow kicker">Lanterns Along the Hidden Stair</p>
    <h1 class="glow headline">Of Every Soul:</h1>
    <p class="glow subline subline-1">Gathered</p>
    <p class="glow subline subline-2">from Voices Dwelling</p>
    <h2 class="glow main-title">In the Further Meadow</h2>
    <p class="author">T. Morven Ashdale</p>
  </main>
</body>
</html>
```